Fun, Bright Company needs Packaging Design for Tin Box!

Hello! We are looking for a design for a tin box (template attached.)
This tin box will hold a set of 3 bath bombs. On the top of the box, there should be text that reads "Sunny, Pickle". On the back of the box, the details should read "Set of 3 bath bombs", "Reusable tin!", have a barcode place holder, and have our logo (also attached).
This product is able to be print in full color,.
You can see our design inspiration here: https://www.moodquilt.example/lanternmoth/design-inspo/

```html
<!DOCTYPE html>
<html lang="en">
<head>
<meta charset="utf-8">
<title>Joy League – Sunny, Pickle Bath Bomb Tin</title>
<link rel="stylesheet" href="https://fonts.googleapis.com/css2?family=Roboto+Condensed:wght@400;800;900&family=Oswald:wght@300&family=Poppins:wght@400&display=swap">
<style>
  :root{
    --page:#ffffff;
    --ink:#111111;
    --dieline:#e0402e;
    --teal:#6cb9bb;
    --sky:#71ccee;
    --bubble:#4ec4f0;
    --tin-blue:#47a8d6;
    --pale-blue:#95d6ef;
    --shadow-blue:#3fa6dc;
    --white:#ffffff;
  }
  *{margin:0;padding:0;box-sizing:border-box}
  html,body{width:1200px;height:2383px;overflow:hidden;background:var(--page)}
  body{position:relative;font-family:"Roboto Condensed",sans-serif;color:var(--ink)}
  .abs{position:absolute}

  /* Lid */
  .lid{left:216px;top:95px;width:702px;height:464px;overflow:hidden}
  .lid-art{position:absolute;inset:0;
    background:
      radial-gradient(ellipse 170px 130px at 95% 5%, var(--white) 60%, transparent 62%),
      radial-gradient(ellipse 140px 60px at 10% 0%, var(--white) 60%, transparent 62%),
      radial-gradient(ellipse 160px 140px at 8% 95%, var(--bubble) 60%, transparent 62%),
      radial-gradient(ellipse 140px 120px at 92% 92%, var(--bubble) 60%, transparent 62%),
      linear-gradient(100deg, var(--teal) 0%, var(--teal) 38%, var(--sky) 55%, var(--teal) 72%, var(--teal) 100%)}
  .brand-pill{left:205px;top:103px;width:295px;height:52px;border:3px solid var(--white);border-radius:26px;
    display:flex;align-items:center;justify-content:center;
    font-weight:900;font-size:38px;letter-spacing:2px;color:var(--white);text-transform:uppercase}
  .lid-title{left:0;width:100%;top:190px;text-align:center;font-weight:900;font-size:92px;line-height:1;
    color:var(--white);letter-spacing:-1px;text-shadow:5px 5px 0 var(--shadow-blue);text-transform:uppercase}
  .lid-sub{left:0;width:100%;top:318px;text-align:center;font-family:"Oswald",sans-serif;font-weight:300;
    font-size:40px;color:var(--white);letter-spacing:0}

  .dieline{position:absolute;border:1px solid var(--dieline)}
  .rule-v{position:absolute;width:1px;background:var(--dieline)}
  .rule-h{position:absolute;height:1px;background:var(--dieline)}

  .dim{position:absolute;font-family:"Poppins",sans-serif;font-size:28px;color:var(--ink);line-height:1}
  .dim.rot{transform:rotate(-90deg);transform-origin:center}

  /* Base */
  .base{left:76px;top:651px;width:992px;height:753px;background:var(--tin-blue)}
  .back-panel{left:280px;top:856px;width:584px;height:342px;overflow:hidden;
    background:
      radial-gradient(ellipse 120px 45px at 15% 2%, var(--white) 60%, transparent 62%),
      radial-gradient(ellipse 60px 70px at 100% 10%, var(--bubble) 60%, transparent 62%),
      var(--teal)}
  .brand-tag{left:350px;top:16px;width:216px;height:42px;background:var(--white);border-radius:4px;
    display:flex;align-items:center;justify-content:center;font-weight:900;font-size:30px;letter-spacing:2px;
    color:var(--tin-blue);text-transform:uppercase}
  .back-kicker{left:23px;top:78px;font-weight:800;font-size:64px;line-height:1;color:var(--pale-blue);
    letter-spacing:-2px;text-shadow:3px 3px 0 var(--shadow-blue);text-transform:uppercase}
  .back-title{left:25px;top:140px;font-weight:900;font-size:80px;line-height:1;color:var(--white);
    letter-spacing:0;text-shadow:5px 5px 0 var(--shadow-blue);text-transform:uppercase}
  .back-note{left:27px;top:300px;font-family:"Poppins",sans-serif;font-size:19px;color:var(--white);letter-spacing:.5px}
  .code-space{left:373px;top:231px;width:200px;height:100px;background:var(--white)}
</style>
</head>
<body>

<section class="abs lid" aria-label="Tin lid artwork">
  <div class="lid-art" role="img" aria-label="Illustrated sky with clouds, a winding blue stream and bubbles"></div>
  <div class="abs brand-pill">Joy League</div>
  <h1 class="abs lid-title">Sunny, Pickle</h1>
  <p class="abs lid-sub">BATH BOMBS</p>
</section>
<div class="dieline" style="left:216px;top:98px;width:44px;height:461px"></div>
<div class="dieline" style="left:875px;top:95px;width:43px;height:464px"></div>
<div class="dieline" style="left:260px;top:95px;width:615px;height:464px"></div>
<div class="rule-h" style="left:260px;top:138px;width:615px"></div>
<div class="rule-h" style="left:260px;top:515px;width:615px"></div>
<div class="dim" style="left:563px;top:564px">7.08</div>
<div class="dim rot" style="left:918px;top:292px">4.33″</div>

<section class="abs base" aria-label="Tin base dieline"></section>
<div class="dieline" style="left:264px;top:651px;width:616px;height:753px"></div>
<div class="rule-h" style="left:76px;top:839px;width:992px"></div>
<div class="rule-h" style="left:76px;top:1216px;width:992px"></div>
<div class="rule-v" style="left:76px;top:839px;height:377px"></div>
<div class="rule-v" style="left:1068px;top:839px;height:377px"></div>
<div class="dim" style="left:942px;top:808px">2.17″</div>

<section class="abs back-panel" aria-label="Tin back panel">
  <div class="abs brand-tag">Joy League</div>
  <p class="abs back-kicker">Set of 3</p>
  <h2 class="abs back-title">Bath Bombs</h2>
  <p class="abs back-note">REUSABLE TIN!</p>
  <div class="abs code-space" aria-label="Product code space"></div>
</section>
<div class="dim" style="left:551px;top:1170px">7.08</div>
<div class="dim rot" style="left:826px;top:992px">4.33″</div>

</body>
</html>
```